Elegant Financial Planning Business Card

Clearpath Wealth Advisory Pty Ltd requires an elegant business card that communicates simplicity, elegance and trust.
Attached card example of 'Varnoth' is very close to what I am looking for. Looking for black and white card.
Update 24/1/16: The attached Varnoth card is almost exactly what I am looking for. Although it is possible that alternative layouts may interest me, it is considerably more likely that I will proceed with a virtual clone of the "Varnoth' example.
Industry/Entity Type
Financial Planning
Contact Information for Business Card
In black font...
Front Details are (layout as per Dana Varnoth card picture):
Line1 - Name: Oliver Marsh
Line 2 - Company: Clearpath Wealth Advisory Pty Ltd
Line 3 - Address: Harbourview Plaza 3, Level 17, 58 Lomond Avenue, Ellery Heights VIC
Line 4
- Phone: 136 712
- Email: advice@cpwa-example.com.au
- Site: www.cpwa-example.com.au
Back details
1/ logo in position and dimensions as per attached layout
2. Bottom left (in smaller writing).
- Authorised Representative No. 517946
- Clearpath Wealth Advisory is a corporate authorised representative of Tarquay7 Capital Services Pty Ltd
- ABN 47 318 602 154
- AFSL No. 608139

```html
<!DOCTYPE html>
<html lang="en">
<head>
<meta charset="utf-8">
<title>Clearpath Wealth Advisory – Business Card</title>
<link href="https://fonts.googleapis.com/css2?family=Tinos:wght@400;700&display=swap" rel="stylesheet">
<style>
  :root {
    --ink: #111111;
    --card-black: #0d0d0d;
    --paper: #ffffff;
    --rule-light: #8a8a8a;
    --rule-dark: #333333;
    --text-muted: #cfcfcf;
    --text-grey: #555555;
    --stage: #e9e7e3;
  }
  * { box-sizing: border-box; margin: 0; padding: 0; }
  html, body {
    width: 1200px; height: 913px; overflow: hidden;
    background: var(--stage);
    font-family: "Tinos", "Times New Roman", serif;
  }
  .stage {
    width: 1200px; height: 913px;
    display: flex; align-items: center; justify-content: center; gap: 40px;
  }
  .card {
    position: relative;
    width: 540px; height: 309px;
    border-radius: 16px;
    box-shadow: 0 6px 18px rgba(0,0,0,.18);
    overflow: hidden;
  }

  /* ---------- Front ---------- */
  .card--front { background: var(--card-black); color: var(--paper); }
  .front__person {
    position: absolute; left: 26px; top: 24px;
    display: flex; align-items: flex-start; gap: 10px;
  }
  .front__person-mark { width: 14px; height: 30px; background: var(--paper); }
  .front__name { font-size: 18px; font-weight: 700; line-height: 1; }
  .front__role { font-size: 11px; color: var(--text-muted); margin-top: 4px; }

  .front__brand {
    position: absolute; right: 30px; top: 26px;
    font-size: 44px; line-height: 1; color: var(--paper);
  }
  .front__rule-top {
    position: absolute; left: 200px; right: 30px; top: 96px;
    height: 1px; background: var(--rule-light);
  }
  .front__contact {
    position: absolute; right: 30px; top: 110px;
    list-style: none; text-align: right;
    font-size: 11.5px; line-height: 18px;
  }
  .front__contact li { display: flex; align-items: center; justify-content: flex-end; gap: 7px; }
  .front__contact svg { width: 10px; height: 10px; fill: var(--paper); }

  .front__company { position: absolute; left: 30px; top: 176px; }
  .front__company-main { font-size: 30px; letter-spacing: .5px; line-height: 1; }
  .front__company-sub { font-size: 15px; letter-spacing: .6px; margin-top: 2px; }
  .front__rule-bottom {
    position: absolute; left: 30px; width: 240px; top: 232px;
    height: 1px; background: var(--rule-light);
  }
  .front__address {
    position: absolute; left: 30px; top: 246px;
    font-style: normal;
    font-size: 12px; line-height: 17px; color: var(--text-muted);
  }

  /* ---------- Back ---------- */
  .card--back { background: var(--paper); color: var(--ink); }
  .back__corner {
    position: absolute; right: 0; top: 0;
    width: 18px; height: 18px; background: var(--ink);
  }
  .back__registration {
    position: absolute; right: 34px; top: 26px;
    text-align: right; font-size: 10px; line-height: 13px; color: var(--text-grey);
  }
  .back__rule-top {
    position: absolute; left: 180px; right: 30px; top: 70px;
    height: 1px; background: var(--rule-dark);
  }
  .back__brand {
    position: absolute; left: 30px; top: 110px;
    font-size: 50px; line-height: 1;
  }
  .back__company { position: absolute; left: 30px; top: 172px; }
  .back__company-main { font-size: 20px; letter-spacing: .4px; line-height: 1; }
  .back__company-sub { font-size: 11px; letter-spacing: .4px; margin-top: 1px; }
  .back__rule-bottom {
    position: absolute; left: 30px; width: 300px; top: 212px;
    height: 1px; background: var(--rule-dark);
  }
  .back__disclosure {
    position: absolute; left: 30px; top: 222px; width: 470px;
    font-size: 11px; font-weight: 700; line-height: 15px;
  }
</style>
</head>
<body>
<main class="stage">

  <section class="card card--front" aria-label="Business card front">
    <div class="front__person">
      <span class="front__person-mark"></span>
      <div>
        <p class="front__name">Oliver Marsh</p>
        <p class="front__role">Director</p>
      </div>
    </div>

    <p class="front__brand">Clearpath</p>
    <span class="front__rule-top"></span>

    <ul class="front__contact">
      <li>136 712
        <svg viewBox="0 0 24 24" aria-hidden="true"><path d="M6.6 10.8a15 15 0 0 0 6.6 6.6l2.2-2.2c.3-.3.7-.4 1-.2 1.1.4 2.3.6 3.6.6.6 0 1 .4 1 1V20c0 .6-.4 1-1 1A17 17 0 0 1 3 4c0-.6.4-1 1-1h3.5c.6 0 1 .4 1 1 0 1.3.2 2.5.6 3.6.1.3 0 .7-.2 1z"/></svg>
      </li>
      <li>advice@cpwa-example.com.au
        <svg viewBox="0 0 24 24" aria-hidden="true"><path d="M2 5h20v14H2zm2 2v.5l8 5 8-5V7l-8 5z"/></svg>
      </li>
      <li>www.cpwa-example.com.au
        <svg viewBox="0 0 24 24" aria-hidden="true"><path d="M12 2a10 10 0 1 0 0 20 10 10 0 0 0 0-20zm6.9 9h-3a15 15 0 0 0-1.3-5.6A8 8 0 0 1 18.9 11zM12 4.1c.9 1.2 1.7 3.8 1.9 6.9h-3.8c.2-3.1 1-5.7 1.9-6.9zM9.4 5.4A15 15 0 0 0 8.1 11h-3a8 8 0 0 1 4.3-5.6zM5.1 13h3a15 15 0 0 0 1.3 5.6A8 8 0 0 1 5.1 13zm6.9 6.9c-.9-1.2-1.7-3.8-1.9-6.9h3.8c-.2 3.1-1 5.7-1.9 6.9zm2.6-1.3a15 15 0 0 0 1.3-5.6h3a8 8 0 0 1-4.3 5.6z"/></svg>
      </li>
    </ul>

    <div class="front__company">
      <p class="front__company-main">CLEARPATH</p>
      <p class="front__company-sub">Wealth Advisory Pty Ltd</p>
    </div>
    <span class="front__rule-bottom"></span>
    <address class="front__address">
      Harbourview Plaza 3, Level 17, 58<br>
      Lomond Avenue, Ellery Heights VIC
    </address>
  </section>

  <section class="card card--back" aria-label="Business card back">
    <span class="back__corner"></span>
    <div class="back__registration">
      <p>ABN 47 318 602 154</p>
      <p>AFSL No. 608139</p>
    </div>
    <span class="back__rule-top"></span>

    <p class="back__brand">Clearpath</p>
    <div class="back__company">
      <p class="back__company-main">CLEARPATH</p>
      <p class="back__company-sub">Wealth Advisory Pty Ltd</p>
    </div>
    <span class="back__rule-bottom"></span>
    <div class="back__disclosure">
      <p>Authorised Representative No. 517946</p>
      <p>Clearpath Wealth Advisory is a corporate authorised representative of Tarquay7 Capital Services Pty Ltd</p>
    </div>
  </section>

</main>
</body>
</html>
```